Web Design Project

Create a web design

Target Market(s)

Upper class people interested in health

Requirements
Must have
• Templates
Nice to have
• Use the logo provided

```html
<!DOCTYPE html>
<html lang="en">
<head>
<meta charset="utf-8">
<title>Equilio – Your daily activity</title>
<link href="https://fonts.googleapis.com/css2?family=Maven+Pro:wght@400;500;600&display=swap" rel="stylesheet">
<style>
  :root{
    --page:#eceef0;
    --panel:#f7f8f9;
    --line:#d8dbde;
    --text:#5c5f63;
    --heading:#55585c;
    --muted:#8d9196;
    --blue:#5b9dcc;
    --blue-dark:#3f82b4;
    --orange:#e8a93c;
    --red:#d9534f;
    --white:#ffffff;
  }
  *{box-sizing:border-box;margin:0;padding:0}
  html,body{width:1200px;height:1030px;overflow:hidden}
  body{
    background:radial-gradient(ellipse at 50% 35%,#fbfbfc 0%,#eef0f2 60%,#e6e8ea 100%);
    font-family:"Maven Pro",sans-serif;color:var(--text);position:relative;
  }
  .abs{position:absolute}

  /* header */
  .top-links{top:27px;right:168px;font-size:14px;display:flex}
  .top-links a{color:var(--blue);text-decoration:none;padding:0 9px;border-left:1px solid var(--line)}
  .top-links a:first-child{border-left:none}
  .top-links a:last-child{color:var(--muted);padding-right:0}
  .brand{left:57px;top:68px;display:flex;align-items:center;gap:14px}
  .brand-dot{width:44px;height:44px;border-radius:50%;background:var(--orange)}
  .brand-name{font-size:50px;font-weight:400;color:#7d8084;letter-spacing:.5px}
  .social{top:96px;right:178px;display:flex}
  .social span{width:44px;display:flex;justify-content:center;border-left:1px solid var(--line)}
  .social span:first-child{border-left:none}
  .social i{display:block;width:14px;height:14px;border-radius:50%;border:1.5px solid #b9bcc0}

  /* nav */
  .nav{left:57px;top:156px;width:975px;height:45px;background:linear-gradient(#fdfdfd,#eef0f1);
    border:1px solid #d3d6d9;border-radius:3px;box-shadow:0 3px 6px rgba(0,0,0,.12);display:flex}
  .nav-item{height:100%;display:flex;flex-direction:column;justify-content:center;align-items:center;
    padding:0 18px;border-right:1px solid var(--line);font-size:12px;letter-spacing:.6px;color:#6a6e72;text-transform:uppercase}
  .nav-item .bar{display:block;height:3px;width:100%;background:#c9ccd0;margin-top:6px}
  .nav-item.active{background:var(--white);color:var(--blue-dark)}
  .nav-item.active .bar{background:var(--blue)}
  .nav-item small{font-size:8px;letter-spacing:.3px;line-height:1}
  .nav-item .row{display:flex;align-items:center;gap:6px}
  .nav-item .row .disc{width:20px;height:20px;border-radius:50%;background:#6c8fae}
  .search{position:absolute;right:9px;top:7px;width:201px;height:26px;border:1px solid #c5c8cc;border-radius:3px;
    background:linear-gradient(#e9ebed,#f6f7f8);display:flex;align-items:center;gap:7px;padding-left:8px;font-size:12px;color:#8a8e92;letter-spacing:.5px}

  /* hero */
  .hero-title{left:117px;top:274px;font-size:40px;font-weight:400;color:var(--heading);letter-spacing:.5px}
  .hero-sub{left:117px;top:323px;font-size:25px;color:var(--blue);letter-spacing:.4px}
  .arrow{top:400px;width:38px;height:38px;border-radius:50%;background:linear-gradient(#fff,#dfe2e5);
    border:1px solid #b8bcc0;box-shadow:0 1px 3px rgba(0,0,0,.2);display:flex;align-items:center;justify-content:center}
  .arrow.prev{left:9px}.arrow.next{left:1043px}
  .stat-icons{left:134px;top:399px;display:flex;gap:27px}
  .stat-icon{width:73px;height:73px;border-radius:50%;background:var(--white);border:2px solid #c9d9e6;padding:3px}
  .stat-icon svg{display:block}
  .stats{left:117px;top:483px;width:518px;height:83px;background:var(--blue);border-radius:3px;display:flex;padding-left:11px}
  .stat{width:100px;text-align:center;color:var(--white);padding-top:8px}
  .stat b{display:block;font-size:31px;font-weight:500;letter-spacing:1px;line-height:1.1}
  .stat span{display:block;font-size:11px;line-height:1.25}
  .hero-photo{left:616px;top:226px;width:392px;height:378px;border-radius:4px;
    background:radial-gradient(ellipse at 45% 40%,#e9d4c6 0%,#d9c3cf 45%,#c7a7e0 70%,rgba(236,238,240,0) 100%)}
  .dots{left:479px;top:638px;display:flex;gap:10px}
  .dots i{display:block;width:37px;height:11px;border-radius:3px;background:linear-gradient(#fff,#e3e5e8);border:1px solid #c4c7cb}
  .dots i.on{background:#bfc2c6}

  /* cards */
  .card{top:675px;width:318px;height:380px;background:var(--panel);border:1px solid #d6d9dc;border-radius:3px;
    box-shadow:0 1px 3px rgba(0,0,0,.06);padding:0 20px}
  .card-1{left:57px}.card-2{left:386px}.card-3{left:715px}
  .badge{position:absolute;right:12px;top:0;height:26px;padding:0 11px;color:var(--white);font-size:12px;font-weight:600;
    display:flex;align-items:center;border-radius:0 0 3px 3px;letter-spacing:.5px}
  .badge.new{background:var(--blue)}.badge.top{background:var(--orange)}.badge.hot{background:var(--red)}
  .card h2{font-size:24px;font-weight:400;color:var(--heading);padding-top:16px;padding-bottom:8px;border-bottom:3px solid var(--blue);letter-spacing:.3px}
  .card-media{position:relative;margin-top:12px;height:170px;overflow:hidden}
  .bubble{position:absolute;border-radius:50%;color:var(--white);text-align:center;display:flex;flex-direction:column;justify-content:center}
  .bubble b{font-size:30px;font-weight:500;line-height:1}
  .bubble span{font-size:12px}
  .sleep-bubble{left:-30px;top:-70px;width:180px;height:180px;background:rgba(91,157,204,.85);
    justify-content:flex-start;align-items:flex-start;text-align:left;padding:78px 0 0 43px}
  .sleep-bubble b{font-size:34px}
  .sleep-bubble span{font-size:11px;margin-top:2px;white-space:nowrap}
  .card p{font-size:14px;line-height:1.5;margin-top:19px;color:var(--text);max-width:262px}
  .read-more{display:inline-flex;align-items:center;margin-top:18px;height:25px;border:1px solid #c7cacd;border-radius:2px;
    background:linear-gradient(#fff,#eceef0);font-size:11px;color:#5a5e62;letter-spacing:.4px}
  .read-more em{font-style:normal;width:22px;text-align:center;border-right:1px solid #d2d5d8;color:#999;height:100%;line-height:23px}
  .read-more span{padding:0 10px 0 9px}
</style>
</head>
<body>

<nav class="top-links abs"><a>Features</a><a>Typography</a><a>News</a></nav>

<div class="brand abs"><span class="brand-dot"></span><span class="brand-name">Equilio</span></div>

<div class="social abs" aria-label="Social links"><span><i></i></span><span><i></i></span><span><i></i></span><span><i></i></span><span><i></i></span></div>

<nav class="nav abs">
  <div class="nav-item active">Home<span class="bar"></span></div>
  <div class="nav-item">Features<span class="bar"></span></div>
  <div class="nav-item">Toolkit<span class="bar"></span></div>
  <div class="nav-item">Icons<span class="bar"></span></div>
  <div class="nav-item"><div class="row"><span class="disc"></span><div>Blogroll<br><small>Categories</small></div></div><span class="bar"></span></div>
  <div class="nav-item"><div>Module<br><small>Menu position</small></div><span class="bar"></span></div>
  <div class="search">
    <svg width="12" height="12" viewBox="0 0 12 12"><circle cx="5" cy="5" r="3.6" fill="none" stroke="#888" stroke-width="1.6"/><line x1="7.6" y1="7.6" x2="11" y2="11" stroke="#888" stroke-width="1.8"/></svg>
    search...
  </div>
</nav>

<h1 class="hero-title abs">Your daily activity</h1>
<p class="hero-sub abs">Increase your efficiency</p>

<div class="arrow prev abs"><svg width="10" height="10" viewBox="0 0 10 10"><path d="M7 1 3 5l4 4" fill="none" stroke="#777" stroke-width="1.8"/></svg></div>
<div class="arrow next abs"><svg width="10" height="10" viewBox="0 0 10 10"><path d="M3 1l4 4-4 4" fill="none" stroke="#777" stroke-width="1.8"/></svg></div>

<div class="hero-photo abs" role="img" aria-label="Smiling woman stretching on a purple yoga mat"></div>

<div class="stat-icons abs">
  <div class="stat-icon"><svg width="63" height="63" viewBox="0 0 64 64"><circle cx="32" cy="32" r="32" fill="var(--blue)"/><circle cx="32" cy="35" r="13" fill="#fff"/><rect x="31" y="16" width="3" height="8" rx="1.5" fill="#fff"/></svg></div>
  <div class="stat-icon"><svg width="63" height="63" viewBox="0 0 64 64"><circle cx="32" cy="32" r="32" fill="var(--orange)"/><path d="M32 32V0A32 32 0 0 1 64 32Z" fill="var(--blue)"/><circle cx="32" cy="35" r="13" fill="#fff"/><circle cx="29" cy="35" r="1.6" fill="var(--orange)"/><circle cx="35" cy="35" r="1.6" fill="var(--orange)"/></svg></div>
  <div class="stat-icon"><svg width="63" height="63" viewBox="0 0 64 64"><circle cx="32" cy="32" r="32" fill="var(--blue)"/><path d="M32 32V0A32 32 0 0 1 32 64Z" fill="var(--orange)"/><circle cx="32" cy="32" r="22" fill="#fff"/><circle cx="32" cy="32" r="1.6" fill="#888"/></svg></div>
  <div class="stat-icon"><svg width="63" height="63" viewBox="0 0 64 64"><circle cx="32" cy="32" r="32" fill="var(--blue)"/><path d="M24 46l6-10 5 4 3 8M30 36l2-11 8 3 4 6M32 25l-8 4-3 6" fill="none" stroke="#fff" stroke-width="4" stroke-linecap="round" stroke-linejoin="round"/><circle cx="38" cy="17" r="4" fill="#fff"/></svg></div>
  <div class="stat-icon"><svg width="63" height="63" viewBox="0 0 64 64"><circle cx="32" cy="32" r="32" fill="var(--blue)"/><circle cx="32" cy="32" r="28" fill="var(--orange)"/><path d="M32 32V4A28 28 0 0 0 32 60Z" fill="var(--blue)"/><circle cx="32" cy="32" r="1.6" fill="#fff"/></svg></div>
</div>

<div class="stats abs">
  <div class="stat"><b>720</b><span>Calories<br>consumed</span></div>
  <div class="stat"><b>406</b><span>Calories<br>burned</span></div>
  <div class="stat"><b>25</b><span>Time</span></div>
  <div class="stat"><b>1.5</b><span>Miles</span></div>
  <div class="stat"><b>8:00</b><span>Sleep</span></div>
</div>

<div class="dots abs"><i></i><i></i><i class="on"></i></div>

<article class="card card-1 abs">
  <span class="badge new">NEW</span>
  <h2>Sleep Cycle</h2>
  <div class="card-media" role="img" aria-label="Woman sleeping peacefully on a white pillow" style="background:linear-gradient(120deg,#cfe0ee 0%,#efe3da 55%,#f5efea 100%)">
    <div class="bubble sleep-bubble">
      <b>75%</b><span>Sleep efficiency</span>
    </div>
  </div>
  <p>Sleep is one of the most important things for your body and your soul.</p>
  <a class="read-more"><em>»</em><span>READ MORE</span></a>
</article>

<article class="card card-2 abs">
  <span class="badge top">TOP</span>
  <h2>Healthy Meal</h2>
  <div class="card-media" role="img" aria-label="Glass bowls of dried fruit and nuts on a green placemat" style="background:linear-gradient(160deg,#b99a7c 0%,#d9b77e 45%,#a8b66a 100%)">
    <div class="bubble" style="left:160px;top:53px;width:106px;height:106px;background:rgba(91,157,204,.92)">
      <b>130.5</b><span>kcal</span>
    </div>
  </div>
  <p>Get some inspiration from one of 90 quick and easy healthy recipe ideas.</p>
  <a class="read-more"><em>»</em><span>READ MORE</span></a>
</article>

<article class="card card-3 abs">
  <span class="badge hot">HOT</span>
  <h2>Sport Activities</h2>
  <div class="card-media" role="img" aria-label="Man jogging outdoors under a blue sky" style="background:linear-gradient(180deg,#8fbfe6 0%,#b7d3ea 50%,#8fa874 100%)">
    <div class="bubble" style="left:6px;top:18px;width:106px;height:106px;background:rgba(91,157,204,.92)">
      <b>4500</b><span>Steps</span>
    </div>
    <div class="bubble" style="left:80px;top:78px;width:86px;height:86px;background:rgba(232,169,60,.92)">
      <b style="font-size:26px">1.5</b><span>Miles</span>
    </div>
  </div>
  <p>Stay well and track your daily fitness and outdoor activity.</p>
  <a class="read-more"><em>»</em><span>READ MORE</span></a>
</article>

</body>
</html>
```